Keen Volt Electrical in need of a business card design

We need a new business card designed for our electrical business. We have a logo already which I will attach below.
Would like the business card to be..
-BLACK background preferably, possibly white back ground behind logo if colours clash.
-White & Blue (logo blue) text
Something that makes the logo pop, & a modern look. Possibly minimal clean format.

REQUIRE:
-Logo on front & back

TEXT TO INCLUDE (ON ONE SIDE):

Tom Harlow
Director/Electrician
M: 0412 563 718
E:info@keenvoltelectrical.com.au
W:www.keenvoltelectrical.com.au
R.E.C 58431

Custom/New Homes
Renovations
Commercial Office/Shop Fit-outs
Communications & Security Cameras
Electric Vehicle Chargers
Airconditioning
Updates

Requirements
Nice to have
• Possibly even lighten the grey shades for the words 'Keen' & 'Volt' to be more easily read on a black background.

```html
<!DOCTYPE html>
<html lang="en">
<head>
<meta charset="utf-8">
<title>Keen Volt Electrical – Business Card</title>
<link rel="stylesheet" href="https://fonts.googleapis.com/css2?family=Open+Sans:wght@400;600&family=Oswald:wght@500&display=swap">
<style>
  :root {
    --canvas: #ffffff;
    --card-black: #000000;
    --card-white: #f6f6f7;
    --brand-blue: #0ea5dc;
    --slate: #2e3a44;
    --slate-mid: #56636d;
    --light-text: #f2f2f2;
    --logo-light: #d6dadd;
  }
  * { margin: 0; padding: 0; box-sizing: border-box; }
  html, body { width: 1200px; height: 1000px; overflow: hidden; background: var(--canvas); }
  body { position: relative; font-family: "Open Sans", sans-serif; }

  .card {
    position: absolute;
    left: 275px;
    width: 676px;
    height: 386px;
    box-shadow: 10px 12px 14px rgba(0,0,0,0.28);
  }
  .card--front { top: 52px; background: var(--card-black); }
  .card--back {
    top: 521px;
    background: linear-gradient(135deg, #ffffff 0%, var(--card-white) 55%, #e9eaeb 100%);
  }

  .brand { position: absolute; display: flex; align-items: center; gap: 20px; }
  .brand__mark { width: 58px; height: 58px; background: var(--brand-blue); flex: none; }
  .brand__name { font-weight: 600; font-size: 36px; letter-spacing: 0.2px; white-space: nowrap; }
  .card--front .brand { left: 140px; top: 130px; }
  .card--front .brand__name { color: var(--logo-light); }
  .card--back .brand { left: 45px; top: 38px; }
  .card--back .brand__mark { width: 72px; height: 72px; }
  .card--back .brand__name { color: var(--slate); font-size: 40px; }

  .services {
    position: absolute;
    left: 0; right: 0;
    color: var(--light-text);
    font-size: 14.5px;
  }
  .services li { position: absolute; list-style: none; white-space: nowrap; }

  .person { position: absolute; left: 44px; top: 180px; }
  .person__name { font-family: "Oswald", sans-serif; font-weight: 500; font-size: 30px; color: var(--slate); line-height: 1.1; }
  .person__role { font-size: 16px; color: var(--slate-mid); margin-top: 4px; }
  .person__licence { font-size: 16px; color: var(--brand-blue); margin-top: 6px; }

  .contact { position: absolute; right: 22px; top: 282px; list-style: none; }
  .contact li {
    display: flex; align-items: center; justify-content: flex-end; gap: 12px;
    font-size: 16.5px; color: var(--slate); height: 28.5px;
  }
  .contact svg { width: 20px; height: 20px; flex: none; }
</style>
</head>
<body>

<section class="card card--front" aria-label="Card front">
  <div class="brand">
    <span class="brand__mark"></span>
    <span class="brand__name">Keen Volt Electrical</span>
  </div>
  <ul class="services">
    <li style="left:57px; top:309px;">Custom/New Homes</li>
    <li style="left:255px; top:309px;">Renovations</li>
    <li style="left:379px; top:309px;">Commercial Office/Shop Fit-outs</li>
    <li style="left:38px; top:339px;">Communications &amp; Security Cameras</li>
    <li style="left:315px; top:339px;">Electric Vehicle Chargers</li>
    <li style="left:513px; top:339px;">Airconditioning</li>
  </ul>
</section>

<section class="card card--back" aria-label="Card back">
  <div class="brand">
    <span class="brand__mark"></span>
    <span class="brand__name">Keen Volt Electrical</span>
  </div>

  <div class="person">
    <p class="person__name">Tom Harlow</p>
    <p class="person__role">Director/Electrician</p>
    <p class="person__licence">R.E.C 58431</p>
  </div>

  <ul class="contact">
    <li>0412 563 718
      <svg viewBox="0 0 20 20" aria-hidden="true"><rect x="5" y="1.5" width="10" height="17" rx="2" fill="none" stroke="var(--brand-blue)" stroke-width="1.6"/><circle cx="10" cy="15.5" r="1" fill="var(--brand-blue)"/></svg>
    </li>
    <li>info@keenvoltelectrical.com.au
      <svg viewBox="0 0 20 20" aria-hidden="true"><rect x="2" y="4.5" width="16" height="11" fill="var(--brand-blue)"/><path d="M2.5 5 L10 11 L17.5 5 M2.5 15 L8 10 M17.5 15 L12 10" fill="none" stroke="#fff" stroke-width="1.2"/></svg>
    </li>
    <li>www.keenvoltelectrical.com.au
      <svg viewBox="0 0 20 20" aria-hidden="true"><g fill="none" stroke="var(--brand-blue)" stroke-width="1.4"><circle cx="10" cy="10" r="8"/><ellipse cx="10" cy="10" rx="3.5" ry="8"/><path d="M2 10 H18 M3.5 6 H16.5 M3.5 14 H16.5"/></g></svg>
    </li>
  </ul>
</section>

</body>
</html>
```